Local Chiropractor Needs Up Scale Webdesign

This website needs to have an upscale look with a very modern feel. Below is the information and websites to reference

Add Logo that is attached

Build a color scheme similar to this website image titled "chiro-1"

Must Include these pages in a horizontal menu bar in this order:
Home, Meet Our Staff, Patient Testimonials, Videos, Work Place Wellness, Contact

Build a "classy looking" Make An Appointment Button into the header with the contact info below

Phone Number:
555-314-2706

Address:
4318 Willow Barn Lane, #215
Maplebrook, ND 58492

This website needs 4 rotating banners. Please reference a layout similar to this for the banners: http://drkelmora.com/. However design it nicer than this website, this website is very boring and doesn't flow with the colors properly

Below are the description for each banner

Rotating Banner #1
Use Image: Pediatrics
Two lines of text. First line title line, second description. Use Latin text for fill

Rotating Banner #2
Use Image: Aging Gracefully

Rotating Banner #3
Use Image: Pregnancy

Rotating Banner #4
Use Image: Athletics

I'd like to see a free consultation box similar to the "chiro-1" image. Fields to include are: First Name, Last Name, Phone Number, Comments.

For the body, please fill it with latin text. Please design a professional body layout. You can include a box in the right column for the hours

Office Hours
Monday: 8:00-11:00, 2:00-5:00
Tuesday: 8:30-11:00, 2:00-5:30
Wednesday: 8:00-11:00, 2:00-5:00
Thursday: 10:00-12:00, 2:30-5:00
Friday: 8:00-10:00, 1:00-5:00
Saturday: Closed
Sunday: Closed

For the footer please design something similar to the: http://drkelmora.com/

Also include in the Footer: Powered by Tandem Pixel Works

```html
<!DOCTYPE html>
<html lang="en">
<head>
<meta charset="utf-8">
<title>Evergreen Vitality Chiropractic Center</title>
<link href="https://fonts.googleapis.com/css2?family=Questrial&family=Arimo:wght@400;700&family=Open+Sans:wght@600;700&display=swap" rel="stylesheet">
<style>
:root{
  --black:#151515;
  --header:#171717;
  --band:#2b2b2b;
  --card:#474747;
  --panel:#333333;
  --lime:#c3d932;
  --lime-dark:#7aa21c;
  --footer:#b7cf2e;
  --orange:#e8940e;
  --amber:#c78f2a;
  --white:#ffffff;
  --ink:#1e1e1e;
  --grey-text:#e6e6e6;
}
*{margin:0;padding:0;box-sizing:border-box}
html,body{width:831px;height:1200px;overflow:hidden;background:var(--black)}
body{position:relative;font-family:"Arimo",Arial,sans-serif;color:var(--white)}
.abs{position:absolute}

/* header */
.site-header{left:0;top:0;width:831px;height:96px;background:var(--header)}
.brand{left:70px;top:26px;display:flex;align-items:center;gap:10px}
.brand-dot{width:34px;height:34px;border-radius:50%;background:var(--lime)}
.brand-name{font-family:"Questrial",sans-serif;font-size:21px;color:var(--lime);line-height:1.05}
.brand-name small{display:block;font-size:12px}
.call{left:468px;top:28px;display:flex;align-items:center;gap:6px}
.call-label{font-family:"Questrial",sans-serif;font-size:16px;line-height:1.05;color:var(--lime);font-weight:700}
.call-label span{display:block;color:var(--white);font-weight:400;font-size:16px}
.appointment{left:626px;top:28px;width:136px;height:39px;border-radius:4px;background:linear-gradient(#d6ea55,#8db61f);border:2px solid #e9f3b5;color:#2e4406;font-family:"Open Sans",sans-serif;line-height:1}
.appointment small{position:absolute;left:10px;top:7px;font-size:7.5px;font-weight:600;color:#fff}
.appointment b{position:absolute;left:8px;top:17px;font-size:11px;letter-spacing:-.2px}
.appointment svg{position:absolute;right:4px;top:5px}

/* nav */
.main-nav{left:0;top:96px;width:831px;height:30px;background:var(--lime)}
.main-nav a{position:absolute;top:0;height:30px;line-height:30px;font-size:10.5px;color:var(--ink);text-decoration:none;text-transform:uppercase}
.main-nav a.current{background:var(--orange);color:#fff;padding:0 14px;left:70px}

/* hero */
.hero{left:0;top:126px;width:831px;height:356px;background:linear-gradient(90deg,#6b4a1e 0%,#8aa03a 30%,#c6d27a 50%,#9bb043 70%,#5e4a22 100%)}
.hero-caption{left:70px;top:280px;width:448px;height:67px;background:rgba(255,255,255,.3)}
.hero-caption h1{position:absolute;left:7px;top:9px;font-family:"Open Sans",sans-serif;font-weight:700;font-size:18.5px;color:#3c5a10;letter-spacing:-.3px}
.hero-caption p{position:absolute;left:9px;top:36px;font-family:"Open Sans",sans-serif;font-weight:600;font-size:12px;color:#111}

/* feature band */
.feature-band{left:0;top:482px;width:831px;height:220px;background:var(--band)}
.feature-card{top:438px;width:207px;height:246px;background:rgba(72,72,72,.94);border:1px solid #5a5a5a;text-align:center}
.feature-icon{position:absolute;left:59px;top:8px;width:88px;height:88px;border-radius:50%;background:var(--orange);border:4px solid #b8b0a5;display:flex;align-items:center;justify-content:center}
.feature-card h2{position:absolute;left:0;width:100%;font-family:"Questrial",sans-serif;font-weight:400;font-size:17px}
.feature-card p{position:absolute;left:8px;width:189px;font-size:9.4px;line-height:12.3px;color:var(--grey-text)}
.more{position:absolute;left:62px;top:207px;width:80px;height:24px;line-height:24px;font-family:"Open Sans",sans-serif;font-weight:700;font-size:12px;color:#2d2d2d;background:var(--lime);text-decoration:none}
.more.alt{background:#d18a10;color:#fff}

/* body */
.tab{top:722px;height:28px;font-family:"Questrial",sans-serif;font-size:17px;padding-left:14px;line-height:28px}
.tab-title{left:72px;width:88px;background:var(--panel)}
.tab-technical{left:170px;width:102px;background:var(--lime);color:#fff}
.info-panel{left:72px;top:750px;width:484px;height:178px;background:var(--panel);border-radius:0 3px 3px 3px}
.info-photo{position:absolute;left:8px;top:18px;width:164px;height:110px;background:linear-gradient(135deg,#f4f0ea,#d9d3cb 60%,#bfb7ad);border:2px solid #e6e6e6}
.info-panel h3{position:absolute;left:184px;top:19px;font-family:"Questrial",sans-serif;font-weight:700;font-size:18px;color:#7db52a}
.info-panel .lead{position:absolute;left:185px;top:43px;width:268px;font-size:9.3px;line-height:15.2px;text-align:justify}
.info-panel .rest{position:absolute;left:8px;top:140px;width:470px;font-size:9.3px;line-height:14px}
.hours{left:582px;top:722px;width:180px;height:207px;background:var(--amber);border-radius:4px}
.hours h3{position:absolute;left:10px;top:8px;font-family:"Questrial",sans-serif;font-weight:700;font-size:17.5px}
.hours ul{position:absolute;left:12px;top:34px;width:158px;list-style:none}
.hours li{height:24.3px;line-height:24px;font-size:9.6px;border-bottom:1px solid rgba(255,255,255,.22)}
.hours li:last-child{border-bottom:0}

/* footer */
.site-footer{left:0;top:976px;width:831px;height:186px;background:var(--footer);color:var(--ink)}
.site-footer h4{position:absolute;font-family:"Questrial",sans-serif;font-weight:400;font-size:18px}
.contact-lines{position:absolute;left:90px;top:50px;font-size:9.9px;line-height:15.3px}
.contact-lines a{color:var(--ink)}
.map{position:absolute;left:285px;top:37px;width:172px;height:117px;background:linear-gradient(135deg,#e8e4dc,#d7d2c7);border:3px solid #555}
.field-label{position:absolute;font-size:10px}
.field{position:absolute;left:566px;width:170px;height:22px;background:#fff;border-radius:6px}
.subscribe{position:absolute;left:672px;top:118px;width:57px;height:21px;border-radius:3px;background:var(--orange);font-size:10px;line-height:21px;text-align:center}
.bottom-bar{left:0;top:1162px;width:831px;height:38px;background:var(--header);font-size:9.5px}
.bottom-bar span{position:absolute;top:15px}
</style>
</head>
<body>

<header class="site-header abs">
  <div class="brand abs">
    <div class="brand-dot"></div>
    <div class="brand-name">Evergreen Vitality<small>Chiropractic Center</small></div>
  </div>
  <div class="call abs">
    <svg width="34" height="34" viewBox="0 0 34 34" aria-hidden="true">
      <circle cx="17" cy="17" r="15" fill="none" stroke="#e8940e" stroke-width="2"/>
      <path d="M12 9c-2 2-2 6 2 11s8 6 10 4l-3-3-2 1c-2-1-4-4-5-6l1-2z" fill="#e8940e"/>
    </svg>
    <div class="call-label">Call Us on<span>555-314-2706</span></div>
  </div>
  <div class="appointment abs">
    <small>Click Here to Make an</small><b>APPOINTMENT</b>
    <svg width="26" height="26" viewBox="0 0 30 30" aria-hidden="true">
      <circle cx="15" cy="15" r="13" fill="#fff" stroke="#888" stroke-width="2"/>
      <path d="M15 6v9l6 4" stroke="#333" stroke-width="1.6" fill="none"/>
    </svg>
  </div>
</header>

<nav class="main-nav abs">
  <a class="current" href="#">Home</a>
  <a href="#" style="left:154px">Meet Our Staff</a>
  <a href="#" style="left:282px">Patient Testimonials</a>
  <a href="#" style="left:438px">Videos</a>
  <a href="#" style="left:518px">Work Place Wellness</a>
  <a href="#" style="left:683px">Contact</a>
</nav>

<section class="hero abs" role="img" aria-label="Two older women jogging together along a sunny forest path"></section>
<div class="hero-caption abs">
  <h1>LOREM IPSUM IS SIMPLY DUMMY TEXT</h1>
  <p>Ipsum is simply dummy text of the printing and typesetting industry.</p>
</div>

<section class="feature-band abs"></section>

<article class="feature-card abs" style="left:72px">
  <div class="feature-icon">
    <svg width="44" height="40" viewBox="0 0 44 40" aria-hidden="true"><rect x="2" y="2" width="40" height="36" rx="3" fill="#fff"/><rect x="7" y="7" width="30" height="26" fill="#e8940e"/><path d="M9 27l7-9 6 6 6-8 7 9" stroke="#fff" stroke-width="3" fill="none"/></svg>
  </div>
  <h2 style="top:100px">What is this?</h2>
  <p style="top:132px">Aipisicing elit, sed do eiusmod tempo-cididunt ut labore et dolore magna. aliqua. Utder enim sed do eiusmod tempo-cididunt ut labore et ad minim veniam, quis nostrud exercitation des.</p>
  <a class="more" href="#">MORE</a>
</article>

<article class="feature-card abs" style="left:311px">
  <div class="feature-icon">
    <svg width="50" height="44" viewBox="0 0 50 44" aria-hidden="true"><circle cx="18" cy="22" r="5" fill="#fff"/><path d="M4 34c8-8 16 6 24-4s2-14 14-24" stroke="#fff" stroke-width="3.5" fill="none"/><path d="M36 4l9 0-3 9z" fill="#fff"/></svg>
  </div>
  <h2 style="top:103px">What’s is for ?</h2>
  <p style="top:135px">Aipisicing elit, sed do eiusmod tempo-cididunt ut labore et dolore magna. aliqua. Utder enim sed do eiusmod tempo-cididunt ut labore et ad minim veniam, quis nostrud exercitation des.</p>
  <a class="more alt" href="#">MORE</a>
</article>

<article class="feature-card abs" style="left:555px">
  <div class="feature-icon">
    <svg width="44" height="40" viewBox="0 0 44 40" aria-hidden="true"><path d="M6 4h32l4 10v24H2V14z" fill="#fff"/><path d="M2 14h40M22 4v10" stroke="#e8940e" stroke-width="2"/><rect x="27" y="26" width="10" height="4" fill="#e8940e"/></svg>
  </div>
  <h2 style="top:105px">What stage is it at?</h2>
  <p style="top:135px">Aipisicing elit, sed do eiusmod tempo-cididunt ut labore et dolore magna. aliqua. Utder enim sed do eiusmod tempo-cididunt ut labore et ad minim veniam, quis nostrud exercitation des.</p>
  <a class="more" href="#">MORE</a>
</article>

<div class="tab tab-title abs">Tittle</div>
<div class="tab tab-technical abs">Technical</div>
<section class="info-panel abs">
  <div class="info-photo" role="img" aria-label="Young child touching a pregnant mother's belly"></div>
  <h3>Description</h3>
  <p class="lead">simply dummy text of the printing and typesetting industry. Lorem Ipsum has been the industry's standard dummy text ever since the 1500s, when an unknown printer took a galley of type and scrambled it to make a type specimen book. It has survived not only five centuries, but also the leap into electronic typeset-ting, remaining essentially unchanged.</p>
  <p class="rest">It was popularised in the 1960s with the release of Dryline sheets containing Lorem Ipsum passages, and more recently with desktop publishing software like</p>
</section>

<aside class="hours abs">
  <h3>Office Hours</h3>
  <ul>
    <li>Monday: 8:00-11:00, 2:00-5:00</li>
    <li>Tuesday: 8:30-11:00, 2:00-5:30</li>
    <li>Wednesday: 8:00-11:00, 2:00-5:00</li>
    <li>Thursday: 10:00-12:00, 2:30-5:00</li>
    <li>Friday: 8:00-10:00, 1:00-5:00</li>
    <li>Saturday: Closed</li>
    <li>Sunday: Closed</li>
  </ul>
</aside>

<footer class="site-footer abs">
  <h4 style="left:89px;top:20px">Contact</h4>
  <div class="contact-lines">
    4318 Willow Barn Lane, #215<br>
    Maplebrook, ND 58492<br>
    <a href="#">Get Directions</a><br><br>
    Phone: 555-314-2706<br>
    Fax: 555-208-4417<br>
    <a href="#">Email Us</a>
  </div>
  <div class="map" role="img" aria-label="Street map showing the clinic location"></div>
  <h4 style="left:506px;top:20px">Newsletter Sign Up</h4>
  <span class="field-label" style="left:502px;top:58px">First Name:</span>
  <div class="field" style="top:53px"></div>
  <span class="field-label" style="left:530px;top:90px">Email:</span>
  <div class="field" style="top:84px"></div>
  <div class="subscribe">Subscribe</div>
</footer>

<div class="bottom-bar abs">
  <span style="left:88px">© 2014 Copyright -Evergreen Vitality . All rights reserved</span>
  <span style="left:627px;top:17px">Powered by Tandem Pixel Works</span>
</div>

</body>
</html>
```